Automotive eCommerce Business looking for a business card design

Looking for a clean and simple business card design. Our company name is "Harbor Crest Auto" and we are a company specializing in the ecommerce sales of automotive parts, specifically for pick up trucks and large SUVs. Our company colours are red, black, and white.

Feel free to use the logo provided or create a new logo that you seem fit. Looking forward to your creative ideas!

Industry/Entity Type

Automotive

Contact Information for Business Card

We were thinking of a possibly two-sided design featuring just the logo and company name on one side, and personal information on the other side. Single sided designs will be considered as well.

Font styles to use
Serif
Sans Serif
Decorative

Colors
ec1f27
ffffff
000000

Requirements
Must have
• Space for employee's name, title, phone number and email address, along with the company address and website somewhere.

```html
<!DOCTYPE html>
<html lang="en">
<head>
<meta charset="utf-8">
<title>Harbor Crest Auto – Business Card</title>
<link href="https://fonts.googleapis.com/css2?family=Michroma&family=Open+Sans:wght@400;600;700&display=swap" rel="stylesheet">
<style>
  :root {
    --stage: #111111;
    --card-dark: #0b0b0b;
    --card-dark-edge: #1c1c1c;
    --card-light: #ffffff;
    --brand-red: #ec1f27;
    --ink: #1a1a1a;
    --ink-soft: #333333;
    --white: #ffffff;
  }
  * { margin: 0; padding: 0; box-sizing: border-box; }
  html, body {
    width: 1200px;
    height: 1000px;
    overflow: hidden;
    background: var(--stage);
  }
  .stage {
    position: relative;
    width: 1200px;
    height: 1000px;
    display: flex;
    align-items: center;
    justify-content: center;
    gap: 60px;
  }
  .card {
    position: relative;
    width: 500px;
    height: 286px;
    border-radius: 22px;
    overflow: hidden;
  }

  /* Front side */
  .card--front {
    background: linear-gradient(135deg, #1a1a1a 0%, var(--card-dark) 55%, #050505 100%);
    border: 1px solid var(--card-dark-edge);
    display: flex;
    flex-direction: column;
    align-items: center;
    justify-content: center;
    gap: 26px;
  }
  .brand-mark {
    width: 96px;
    height: 96px;
    background: var(--brand-red);
    border-radius: 6px;
  }
  .brand-name {
    font-family: "Michroma", sans-serif;
    font-size: 15px;
    letter-spacing: 2px;
    color: var(--white);
    text-transform: uppercase;
  }

  /* Back side */
  .card--back {
    background: var(--card-light);
  }
  .back-brand {
    position: absolute;
    left: 48px;
    top: 46px;
    width: 140px;
    display: flex;
    flex-direction: column;
    align-items: center;
    gap: 12px;
  }
  .back-brand .brand-mark {
    width: 110px;
    height: 110px;
  }
  .back-brand-name {
    font-family: "Open Sans", sans-serif;
    font-weight: 700;
    font-size: 14px;
    color: var(--brand-red);
    text-align: center;
    white-space: nowrap;
  }
  .contact {
    position: absolute;
    left: 245px;
    top: 72px;
    font-family: "Open Sans", sans-serif;
    color: var(--ink);
  }
  .contact-name {
    font-weight: 700;
    font-size: 27px;
    line-height: 1.05;
    color: var(--brand-red);
  }
  .contact-title {
    font-size: 15px;
    color: var(--ink-soft);
    margin-bottom: 8px;
  }
  .contact-line {
    display: flex;
    align-items: center;
    gap: 8px;
    font-size: 15px;
    line-height: 1.45;
  }
  .contact-line svg {
    width: 12px;
    height: 12px;
    flex: none;
    fill: var(--brand-red);
  }
  .website {
    position: absolute;
    left: 48px;
    bottom: 32px;
    font-family: "Open Sans", sans-serif;
    font-size: 15px;
    letter-spacing: 7px;
    color: var(--ink);
  }
</style>
</head>
<body>
  <main class="stage">
    <section class="card card--front" aria-label="Card front">
      <div class="brand-mark" aria-hidden="true"></div>
      <p class="brand-name">Harbor Crest Auto Ltd</p>
    </section>

    <section class="card card--back" aria-label="Card back">
      <div class="back-brand">
        <div class="brand-mark" aria-hidden="true"></div>
        <p class="back-brand-name">Harbor Crest Auto</p>
      </div>

      <div class="contact">
        <p class="contact-name">Lorem Ipsum</p>
        <p class="contact-title">Owner</p>
        <p class="contact-line">
          <svg viewBox="0 0 24 24" aria-hidden="true"><path d="M6.6 10.8a15.1 15.1 0 0 0 6.6 6.6l2.2-2.2a1 1 0 0 1 1-.25 11.4 11.4 0 0 0 3.6.57 1 1 0 0 1 1 1V20a1 1 0 0 1-1 1A17 17 0 0 1 3 4a1 1 0 0 1 1-1h3.5a1 1 0 0 1 1 1c0 1.25.2 2.45.57 3.57a1 1 0 0 1-.25 1z"/></svg>
          <span>+12 3456 7890</span>
        </p>
        <p class="contact-line">
          <svg viewBox="0 0 24 24" aria-hidden="true"><path d="M2 5h20v14H2z M2 5l10 8 10-8" /></svg>
          <span>yourmailaddress.com</span>
        </p>
      </div>

      <p class="website">WWW.YOURWEBSITE.COM</p>
    </section>
  </main>
</body>
</html>
```